IT Company Business Card Rebranding

We want to modernize our business cards massively. We want to incorporate aspects of our old business card such as the white and geometric design with the blues of another icon. Existing Logo, old business card and icon are all attached.

We are a modern IT company that provides support for new and growing technologies and want our business cards to be modern yet professional.
Updates

Note: Do not use file ICON.png in design. This is just a design we like Added Wednesday, March 9, 2016

Industry/Entity Type

Information Technology

Contact Information for Business Card

Roughly 43 : 26 or 1075 x 650 px

Font styles to use
Serif

Colors
0492cd
3276b5
33a6d7
86cfc6
cfeae6
cee9f5
ffffff

Requirements
Must have
• Modern yet professional
Nice to have
• We would like to incorporate the blues of our existing logo and of the icon provided. Really like the design of the icon.
Should not have
• Too Decorative. Just simple and professional.
• Not have the circle icon, as it is a copyrighted icon, I just like the colors and the geometric design

```html
<!DOCTYPE html>
<html lang="en">
<head>
<meta charset="utf-8">
<title>Rowan Technical Services – Business Card</title>
<link href="https://fonts.googleapis.com/css2?family=Open+Sans:wght@300;400;600;700&display=swap" rel="stylesheet">
<style>
  :root {
    --stage: #1b2228;
    --card-white: #ffffff;
    --card-shade: #f1f3f4;
    --teal-light: #25d2cf;
    --teal-mid: #1bb3c9;
    --blue-deep: #0492cd;
    --logo-grey: #8a9096;
    --logo-blue: #3276b5;
    --text-white: #ffffff;
  }
  * { margin: 0; padding: 0; box-sizing: border-box; }
  html, body {
    width: 1200px;
    height: 1023px;
    overflow: hidden;
    background: var(--stage);
    font-family: "Open Sans", Arial, sans-serif;
  }
  .sheet {
    position: relative;
    width: 1200px;
    height: 1023px;
    display: flex;
    align-items: center;
    justify-content: center;
    gap: 40px;
  }
  .card {
    width: 540px;
    height: 326px;
    border-radius: 4px;
    overflow: hidden;
    position: relative;
    box-shadow: 0 10px 30px rgba(0,0,0,0.45);
  }

  /* Front: white logo side */
  .card-front {
    background: linear-gradient(160deg, var(--card-white) 0%, var(--card-shade) 100%);
    display: flex;
    align-items: center;
    justify-content: center;
  }
  .brand {
    display: flex;
    align-items: center;
    gap: 18px;
  }
  .brand-dot {
    width: 34px;
    height: 34px;
    border-radius: 50%;
    background: var(--logo-blue);
  }
  .brand-name {
    font-size: 30px;
    font-weight: 300;
    letter-spacing: 9px;
    color: var(--logo-grey);
    text-transform: uppercase;
  }

  /* Back: teal contact side */
  .card-back {
    background: linear-gradient(125deg, var(--teal-light) 0%, var(--teal-mid) 45%, var(--blue-deep) 100%);
    color: var(--text-white);
    padding: 70px 0 0 150px;
  }
  .holder-name {
    font-size: 34px;
    font-weight: 700;
    line-height: 1;
    letter-spacing: 1px;
  }
  .holder-role {
    font-size: 17px;
    font-weight: 600;
    margin-top: 4px;
    letter-spacing: 0.5px;
  }
  .role-rule {
    width: 196px;
    height: 2px;
    background: var(--text-white);
    margin: 12px 0 22px;
  }
  .contact-list { list-style: none; }
  .contact-item {
    display: flex;
    align-items: center;
    gap: 10px;
    font-size: 15px;
    font-weight: 600;
    margin-bottom: 12px;
  }
  .contact-icon {
    width: 26px;
    height: 26px;
    flex: none;
  }
</style>
</head>
<body>
  <main class="sheet">
    <section class="card card-front" aria-label="Business card front">
      <div class="brand">
        <span class="brand-dot"></span>
        <span class="brand-name">Nexora IT</span>
      </div>
    </section>

    <section class="card card-back" aria-label="Business card back">
      <h1 class="holder-name">ROWAN</h1>
      <p class="holder-role">TECHNICAL SERVICES</p>
      <div class="role-rule"></div>
      <ul class="contact-list">
        <li class="contact-item">
          <svg class="contact-icon" viewBox="0 0 26 26" aria-hidden="true">
            <circle cx="13" cy="13" r="12" fill="none" stroke="#fff" stroke-width="1.6"/>
            <path d="M9 7.5c-1 .8-1.3 2-.8 3.4 1.1 2.9 3.2 5 6 6.2 1.3.5 2.5.3 3.3-.7l-2.2-2-1.3 1c-1.6-.8-2.8-2-3.6-3.6l1-1.3z" fill="#fff"/>
          </svg>
          <span>xxxxxxxxxx</span>
        </li>
        <li class="contact-item">
          <svg class="contact-icon" viewBox="0 0 26 26" aria-hidden="true">
            <circle cx="13" cy="13" r="12" fill="none" stroke="#fff" stroke-width="1.6"/>
            <rect x="7.5" y="9" width="11" height="8" fill="#fff"/>
            <path d="M7.5 9l5.5 4.5L18.5 9" fill="none" stroke="#1bb3c9" stroke-width="1.2"/>
          </svg>
          <span>email@mailbox.com</span>
        </li>
        <li class="contact-item">
          <svg class="contact-icon" viewBox="0 0 26 26" aria-hidden="true">
            <circle cx="13" cy="13" r="12" fill="none" stroke="#fff" stroke-width="1.6"/>
            <circle cx="13" cy="13" r="6" fill="none" stroke="#fff" stroke-width="1.3"/>
            <ellipse cx="13" cy="13" rx="2.6" ry="6" fill="none" stroke="#fff" stroke-width="1.1"/>
            <line x1="7" y1="13" x2="19" y2="13" stroke="#fff" stroke-width="1.1"/>
          </svg>
          <span>www.nexorait.com</span>
        </li>
      </ul>
    </section>
  </main>
</body>
</html>
```